Real Estate Development, Finance and Fund Management company

We need a business card and logo design for a new company based in Asia called 'Calloway Vance Ltd.'
We provide full service large scale real estate development services, including fund management, project delivery services and acquisitions. We are looking for a bold logo with a strong feeling of security. A good reference would be the Thornvale (www.thornvalehq.com) or Essenby Capital (www.essenbycap.com).
We will need to have the imagery for the cards and logos to be produced for a dark and light background, and for web and print quality.
Initial thoughts are to have silver text on a black or dark grey background but leave that to your discretion.
Final design should communicate stability, financial safety and building on a solid foundation.
NOTE : We are not looking for pictures or clip art. Logo should be primarily from text and anything additional should be limited and tasteful.
Thanks!

```html
<!DOCTYPE html>
<html lang="en">
<head>
<meta charset="utf-8">
<title>Calloway Vance Ltd. — Business Cards</title>
<link rel="stylesheet" href="https://fonts.googleapis.com/css2?family=Cinzel:wght@600&family=Open+Sans:wght@400;600&display=swap">
<style>
  :root {
    --backdrop: #e8e6e3;
    --silver-light: #f2f2f2;
    --silver-mid: #bdbdbd;
    --silver-dark: #8a8a8a;
    --ink: #1c1c1c;
    --card-charcoal: #2e3030;
    --card-black: #0b0b0b;
    --text-silver: #e4e4e4;
    --text-muted: #b9b9b9;
  }
  * { box-sizing: border-box; margin: 0; padding: 0; }
  html, body { width: 1200px; height: 800px; overflow: hidden; }
  body { background: var(--backdrop); position: relative; font-family: "Open Sans", sans-serif; }

  .card { position: absolute; box-shadow: 0 18px 40px rgba(0,0,0,.28); overflow: hidden; }

  /* Back side: brushed silver, vertical */
  .card-back {
    left: 80px; top: 140px; width: 340px; height: 520px;
    background: linear-gradient(160deg, var(--silver-mid) 0%, var(--silver-light) 45%, #d6d6d6 60%, var(--silver-dark) 100%);
  }
  .card-back .wordmark {
    position: absolute; left: 50%; top: 50%;
    transform: translate(-50%, -50%) rotate(90deg);
    width: 420px; text-align: center;
    font-family: "Cinzel", serif; font-weight: 600; color: var(--ink);
    font-size: 44px; line-height: 1.1; letter-spacing: 2px;
  }

  /* Front side: dark with silver band */
  .card-front {
    left: 490px; top: 230px; width: 640px; height: 360px;
    background: var(--card-charcoal);
  }
  .card-front .black-field { position: absolute; inset: 0; }
  .card-front .wordmark {
    position: absolute; left: 36px; top: 28px;
    font-family: "Cinzel", serif; font-weight: 600; color: var(--text-silver);
    font-size: 30px; line-height: 1.1; letter-spacing: 1.5px;
  }
  .holder { position: absolute; left: 36px; top: 128px; }
  .holder-name {
    font-family: "Cinzel", serif; font-weight: 600; color: var(--text-silver);
    font-size: 21px; letter-spacing: 1px;
  }
  .holder-title { font-size: 12px; color: var(--text-muted); margin-top: 2px; }

  .contact { position: absolute; right: 80px; top: 196px; color: var(--text-silver); font-size: 14px; line-height: 1.45; }
  .contact-row { display: flex; align-items: center; gap: 8px; }
  .contact-row svg { width: 14px; height: 14px; flex: none; }

  .silver-band {
    position: absolute; left: 0; right: 0; bottom: 0; height: 46px;
    background: linear-gradient(180deg, #f4f4f4 0%, #cfcfcf 50%, #9d9d9d 100%);
  }
  .website {
    position: absolute; left: 36px; bottom: 12px;
    font-size: 15px; letter-spacing: 3px; color: #333;
  }
  .corner-fold { position: absolute; right: 0; top: 150px; }
</style>
</head>
<body>

  <section class="card card-back" aria-label="Card back">
    <div class="wordmark">Calloway<br>Vance Ltd.</div>
  </section>

  <section class="card card-front" aria-label="Card front">
    <svg class="black-field" width="640" height="360" viewBox="0 0 640 360" aria-hidden="true">
      <defs>
        <linearGradient id="blackFade" x1="0" y1="0" x2="1" y2="1">
          <stop offset="0" stop-color="#050505"/>
          <stop offset="1" stop-color="#1a1a1a"/>
        </linearGradient>
        <linearGradient id="silverEdge" x1="0" y1="0" x2="1" y2="0">
          <stop offset="0" stop-color="#7d7d7d"/>
          <stop offset=".5" stop-color="#f0f0f0"/>
          <stop offset="1" stop-color="#9a9a9a"/>
        </linearGradient>
      </defs>
      <polygon points="300,0 640,0 640,250" fill="url(#blackFade)"/>
      <line x1="300" y1="0" x2="640" y2="250" stroke="url(#silverEdge)" stroke-width="4"/>
    </svg>

    <div class="wordmark">Calloway<br>Vance Ltd.</div>

    <div class="holder">
      <div class="holder-name">DANA WHITFIELD</div>
      <div class="holder-title">Director</div>
    </div>

    <div class="contact">
      <div>P.O Box 2240 Linden Street,</div>
      <div>Eastbay, Any City</div>
      <div class="contact-row">
        <svg viewBox="0 0 14 14" aria-hidden="true"><rect width="14" height="14" rx="2" fill="#e4e4e4"/><path d="M4 3c1 0 1.3 1.6 1.4 2.2.1.5-.7.9-.6 1.3.4 1 1.3 1.9 2.3 2.3.4.1.8-.7 1.3-.6.6.1 2.2.4 2.2 1.4 0 .8-.9 1.4-1.8 1.4C5.7 11 3 8.3 3 4.8 3 3.9 3.4 3 4 3z" fill="#222"/></svg>
        <span>(405) 555-0148</span>
      </div>
      <div class="contact-row">
        <svg viewBox="0 0 14 14" aria-hidden="true"><rect width="14" height="14" rx="2" fill="#e4e4e4"/><rect x="3" y="4" width="8" height="6" fill="none" stroke="#222" stroke-width="1"/><path d="M3 4l4 3 4-3" fill="none" stroke="#222" stroke-width="1"/></svg>
        <span>info@cvance.net</span>
      </div>
    </div>

    <div class="silver-band"></div>
    <div class="website">www.callowayvance.com</div>

    <svg class="corner-fold" width="60" height="80" viewBox="0 0 60 80" aria-hidden="true">
      <defs>
        <linearGradient id="foldSheen" x1="0" y1="0" x2="1" y2="1">
          <stop offset="0" stop-color="#f0f0f0"/>
          <stop offset="1" stop-color="#7a7a7a"/>
        </linearGradient>
      </defs>
      <polygon points="60,0 20,30 60,80" fill="url(#foldSheen)"/>
    </svg>
  </section>

</body>
</html>
```